Official personalized stationery with official coat of arms

I am looking for custom stationery design such as US letter size (8.5 X 11 or 21.6cm X 27.9cm), email signature (email) and envelope for US letter size (standard envelope no. 10 or 10.5cm X 24.5cm). Inspired by my personal coat of arms and my postal address:

4186 rue des Tilleuls
Levis, Quebec, H2K 4P7
Canada

Ideally a discreet design based on the coat of arms of Lucien Morvan but inspired by my mother's original coat of arms.

Something golden and translucent, simple but tasteful, without overemphasizing the green color. The coat of arms should have green, but not the entire structure of the stationery.

I am also looking for a small official thank you card in half letter size.

The design must be with the Lucien Morvan coat of arms and not the full coat of arms

Target Market(s)

For official communication

Industry/Entity Type

Communication officiel et parlementaire

Font styles to use
Other font styles liked:
• J’aime bien l’écriture comme le logo de la maison Delorme la police pour écrire le nom Delorme

Requirements
Must have
• Simplicity and use the Lucien Morvan coat of arms and not the full coat of arms
Nice to have
• Official and royal appearance as it is an official heraldic title of the British crown
Should not have
• Email and website

```html
<!DOCTYPE html>
<html lang="en">
<head>
<meta charset="utf-8">
<title>Morvan Stationery Suite</title>
<link rel="stylesheet" href="https://fonts.googleapis.com/css2?family=Playfair+Display:wght@400&family=Pinyon+Script&display=swap">
<style>
:root{
  --board:#345f2f;
  --paper:#f7f7ee;
  --gold:#a6862d;
  --gold-soft:#c9b16d;
  --ink:#4a4a44;
  --flap:#345f2f;
}
*{margin:0;padding:0;box-sizing:border-box}
html,body{width:1200px;height:1200px;overflow:hidden;background:var(--board)}
body{position:relative;font-family:"Playfair Display",Georgia,serif}
.suite{position:absolute;left:40px;top:198px;width:1338px;height:960px;transform:scale(.837);transform-origin:0 0}
.sheet{position:absolute;background:var(--paper)}
.brand-mark{position:absolute;color:var(--gold);font-family:"Playfair Display",Georgia,serif;font-weight:400;text-align:center;display:flex;align-items:center;justify-content:center;gap:6px}
.brand-mark .dot{width:8px;height:8px;border-radius:50%;background:var(--gold)}
.ornament{position:absolute;background:var(--gold-soft);opacity:.7}
.script{font-family:"Pinyon Script",cursive;color:var(--gold)}

/* letterhead */
.letterhead{left:0;top:0;width:464px;height:633px;color:var(--ink);font-size:7px;line-height:10.3px}
.letterhead .brand-mark{left:0;right:0;top:58px;font-size:22px}
.letterhead .date{position:absolute;right:66px;top:197px}
.letterhead .salutation{position:absolute;left:66px;top:223px}
.letterhead .body{position:absolute;left:66px;top:253px;width:332px;text-align:justify}
.letterhead .body p{margin-bottom:10px}
.letterhead .closing{position:absolute;left:66px;top:429px}
.letterhead .signature{left:58px;top:460px;width:92px;height:48px;background:transparent;border-bottom:1px solid var(--gold-soft);opacity:.8}
.letterhead .signer{position:absolute;left:66px;top:519px}
.fleur{width:10px;height:12px}

/* envelopes */
.envelope-front{left:500px;top:0;width:525px;height:232px}
.envelope-front .brand-mark{left:28px;top:50px;width:80px;font-size:15px}
.return{position:absolute;text-align:center;color:var(--gold)}
.return .script{font-size:12px;line-height:10px;display:block}
.return .addr{font-size:7.2px;line-height:9.5px;margin-top:6px}
.envelope-front .return{left:22px;top:146px;width:120px}
.envelope-back{left:500px;top:286px;width:525px;height:232px}
.envelope-back svg{position:absolute;left:0;top:0}
.seal{left:228px;top:72px;width:68px;height:68px;border-radius:50%;background:var(--paper);font-size:13px}
.envelope-back .return{left:202px;top:146px;width:120px}

/* thank you card */
.thanks-card{left:1060px;top:0;width:278px;height:385px}
.thanks-card .frame{position:absolute;inset:7px;border:1px solid var(--gold)}
.thanks-card .title{position:absolute;left:0;right:0;top:78px;text-align:center;font-size:42px}
.thanks-card .message{position:absolute;left:84px;width:110px;top:148px;text-align:center;color:var(--gold);font-size:6.4px;line-height:9.7px}

/* email signature */
.email-signature{left:0;top:668px;width:1168px;height:292px}
.email-signature .frame{position:absolute;inset:14px 16px;border:1px solid var(--gold)}
.portrait-ring{position:absolute;left:117px;top:49px;width:194px;height:194px;border-radius:50%;border:1.5px solid var(--gold)}
.portrait{position:absolute;left:14px;top:14px;width:164px;height:164px;border-radius:50%;background:radial-gradient(circle at 50% 40%,#e8e6e4 0%,#a9a9ab 60%,#3a3a3c 100%)}
.sig-name{position:absolute;left:366px;top:52px;font-size:42px;line-height:48px}
.sig-role{position:absolute;left:371px;top:106px;font-size:16px;letter-spacing:1px;color:var(--ink)}
.sig-contacts{position:absolute;left:371px;top:148px;list-style:none;font-size:14px;line-height:26px;letter-spacing:.6px;color:var(--ink)}
.sig-contacts li::before{content:"";display:inline-block;width:5px;height:5px;border-radius:50%;background:var(--gold);margin-right:7px;vertical-align:middle}
.email-signature .brand-mark{right:46px;top:58px;width:90px;font-size:18px}
.sig-web{position:absolute;right:46px;top:253px;font-size:13px;letter-spacing:.6px;color:var(--gold)}
</style>
</head>
<body>
<main class="suite">

  <section class="sheet letterhead">
    <div class="brand-mark"><span class="dot"></span>Morvan</div>
    <div class="date">July 03, 2025</div>
    <div class="salutation">Dear Mr/Mrs</div>
    <div class="body">
      <p>Lorem ipsum dolor sit amet, consectetuer adipiscing elit, sed diam nonummy nibh euismod tincidunt ut laoreet dolore magna aliquam erat volutpat. Ut wisi enim ad minim veniam, quis nostrud exerci tation ullamcorper suscipit lobortis nisl ut aliquip ex ea commodo consequat.</p>
      <p>Duis autem vel eum iriure dolor in hendrerit in vulputate velit esse molestie consequat, vel illum dolore eu feugiat nulla facilisis at vero eros et accumsan et iusto odio dignissim qui blandit praesent luptatum zzril delenit augue duis dolore te feugait nulla facilisi. Duis autem vel eum iriure dolor in hendrerit in vulputate velit esse molestie consequat, vel illum dolore eu feugiat nulla facilisis at vero eros et accumsan et iusto odio dignissim qui blandit praesent luptatum zzril delenit augue duis dolore te feugait nulla facilisi.</p>
      <p>Lorem ipsum dolor sit amet, consectetuer adipiscing elit, sed diam nonummy nibh euismod tincidunt ut laoreet dolore magna aliquam erat volutpat. Ut wisi enim ad minim veniam, quis nostrud exerci tation ullamcorper suscipit lobortis nisl ut aliquip ex ea commodo consequat.</p>
    </div>
    <div class="closing">Sincerely,</div>
    <div class="ornament signature" role="img" aria-label="Handwritten signature"></div>
    <div class="signer">Théo Garand</div>
    <div class="ornament fleur" style="left:227px;top:603px" role="img" aria-label="Small fleur-de-lis ornament"></div>
  </section>

  <section class="sheet envelope-front">
    <div class="brand-mark"><span class="dot"></span>Morvan</div>
    <div class="return">
      <span class="script">Official &amp; Parliamentary<br>Communication</span>
      <div class="addr">4186 rue des Tilleuls, Lévis,<br>Quebec, H2K 4P7, Canada</div>
    </div>
  </section>

  <section class="sheet envelope-back">
    <svg width="525" height="232" viewBox="0 0 525 232" aria-hidden="true">
      <polygon points="6,5 519,5 262,108" fill="var(--flap)"/>
    </svg>
    <div class="brand-mark seal"><span>Morvan</span></div>
    <div class="return">
      <span class="script">Official &amp; Parliamentary<br>Communication</span>
      <div class="addr">4186 rue des Tilleuls, Lévis,<br>Quebec, H2K 4P7, Canada</div>
    </div>
  </section>

  <section class="sheet thanks-card">
    <div class="frame"></div>
    <div class="ornament" style="left:6px;top:6px;width:22px;height:16px" role="img" aria-label="Corner flourish"></div>
    <div class="ornament" style="right:6px;top:6px;width:22px;height:16px" role="img" aria-label="Corner flourish"></div>
    <div class="ornament" style="left:6px;bottom:6px;width:22px;height:16px" role="img" aria-label="Corner flourish"></div>
    <div class="ornament" style="right:6px;bottom:6px;width:22px;height:16px" role="img" aria-label="Corner flourish"></div>
    <div class="title script">Thank You</div>
    <p class="message">Duis autem vel eum iriure dolor in hendrerit in vulputate velit esse molestie consequat, vel illum dolore eu feugiat nulla facilisis at vero eros et accumsan et iusto odio dignissim qui blandit praesent luptatum zzril delenit augue duis dolore te feugait nulla facilisi. Duis autem vel eum iriure dolor in hendrerit in vulputate velit esse molestie consequat.</p>
    <div class="ornament fleur" style="left:134px;top:283px" role="img" aria-label="Small fleur-de-lis ornament"></div>
  </section>

  <section class="sheet email-signature">
    <div class="frame"></div>
    <div class="ornament" style="left:10px;top:8px;width:22px;height:16px" role="img" aria-label="Corner flourish"></div>
    <div class="ornament" style="right:10px;top:8px;width:22px;height:16px" role="img" aria-label="Corner flourish"></div>
    <div class="ornament" style="left:10px;bottom:8px;width:22px;height:16px" role="img" aria-label="Corner flourish"></div>
    <div class="ornament" style="right:10px;bottom:8px;width:22px;height:16px" role="img" aria-label="Corner flourish"></div>
    <div class="portrait-ring"><div class="portrait" role="img" aria-label="Portrait photograph of the member of parliament"></div></div>
    <div class="sig-name script">Maëlle Ouimet</div>
    <div class="sig-role">Member of Parliament (Canada)</div>
    <ul class="sig-contacts">
      <li>Phone: +000-555-0148</li>
      <li>E-mail: MaelleOuimet@yourdomain.com</li>
      <li>Adress: Rive-Sud Riding</li>
    </ul>
    <div class="brand-mark"><span class="dot"></span>Morvan</div>
    <div class="sig-web">www.yourwebsite.com</div>
  </section>

</main>
</body>
</html>
```